BrindleStaffing Business Card Design

We are a staffing company finding positions for dedicated nurses and physicians.

Target Market(s)

Business Professionals

Industry/Entity Type

Staffing

Contact Information for Business Card

Gregory Malden
Chairman
417 39th Crescent South
SAINT PETERSBURG FL 33719
813-555-0147 Mobile
813-555-0183 Fax
gmalden@brindlestaffing.example
www.brindlestaffing.example

Font styles to use
Sans Serif

Colors
fbee3e
f04a50
f37122

Requirements
Must have
• Logo Attached, see colors below. We'd like to see Yellow, Orange and Red.

```html
<!DOCTYPE html>
<html lang="en">
<head>
<meta charset="utf-8">
<title>BrindleStaffing Business Card</title>
<link rel="stylesheet" href="https://fonts.googleapis.com/css2?family=Montserrat:wght@500;600;700&family=Roboto:wght@400&display=swap">
<style>
  :root {
    --brand-yellow: #fbee3e;
    --brand-red: #f04a50;
    --brand-orange: #f37122;
    --paper: #ffffff;
    --ink: #1f1f1f;
    --muted: #6a6a6a;
    --backdrop: #e9ebee;
  }
  * { margin: 0; padding: 0; box-sizing: border-box; }
  html, body {
    width: 1200px; height: 900px; overflow: hidden;
    background: var(--backdrop);
  }
  .canvas {
    position: relative; width: 1200px; height: 900px;
    display: flex; flex-direction: column; align-items: center; justify-content: center; gap: 40px;
  }
  .card {
    position: relative; width: 700px; height: 400px;
    background: var(--paper); overflow: hidden;
    box-shadow: 0 6px 18px rgba(0,0,0,0.12);
  }
  .brand-name {
    position: absolute; display: flex; align-items: center;
    font-family: "Montserrat", sans-serif; font-weight: 700;
    color: var(--brand-orange); letter-spacing: -0.02em; white-space: nowrap;
  }
  .brand-dot { border-radius: 50%; background: var(--brand-yellow); flex: none; }
  .card--front .brand-name { left: 0; right: 0; top: 110px; justify-content: center; font-size: 66px; gap: 16px; }
  .card--front .brand-dot { width: 26px; height: 26px; }
  .card--back .brand-name { left: 42px; top: 92px; font-size: 30px; gap: 8px; }
  .card--back .brand-dot { width: 12px; height: 12px; }

  .address-band {
    position: absolute; left: 0; right: 0; height: 36px;
    background: var(--brand-orange); color: var(--paper);
    display: flex; align-items: center; gap: 10px; padding-left: 36px;
    font-family: "Montserrat", sans-serif; font-weight: 500; font-size: 15px;
    letter-spacing: 0.01em; text-transform: uppercase;
  }
  .card--front .address-band { top: 262px; padding-left: 64px; }
  .card--back .address-band { top: 334px; }
  .address-band svg { width: 12px; height: 16px; flex: none; }

  .corner-flag { position: absolute; }
  .corner-flag--top { left: 0; top: 40px; }
  .corner-flag--bottom { right: 0; top: 268px; }

  .person-name {
    position: absolute; left: 318px; top: 98px;
    font-family: "Montserrat", sans-serif; font-weight: 700; font-size: 32px;
    color: var(--brand-red); letter-spacing: 0.03em; text-transform: uppercase;
  }
  .person-title {
    position: absolute; left: 320px; top: 140px;
    font-family: "Montserrat", sans-serif; font-weight: 600; font-size: 16px;
    color: var(--brand-orange); letter-spacing: 0.12em; text-transform: uppercase;
  }
  .contact-list { position: absolute; left: 290px; top: 180px; list-style: none; }
  .contact-item {
    display: flex; align-items: center; gap: 14px; height: 36px;
    font-family: "Roboto", sans-serif; font-size: 19px; color: var(--ink);
  }
  .contact-label { color: var(--muted); font-size: 15px; margin-left: -6px; }
  .contact-icon { width: 28px; height: 28px; flex: none; }
</style>
</head>
<body>
<main class="canvas">

  <section class="card card--front" aria-label="Business card front">
    <div class="brand-name"><span class="brand-dot"></span>BrindleStaffing</div>
    <div class="address-band">
      <svg viewBox="0 0 12 16"><path d="M6 0a6 6 0 0 0-6 6c0 4.5 6 10 6 10s6-5.5 6-10a6 6 0 0 0-6-6zm0 8.5a2.5 2.5 0 1 1 0-5 2.5 2.5 0 0 1 0 5z" fill="#fff"/></svg>
      417 39th Crescent South, Saint Petersburg FL 33719
    </div>
  </section>

  <section class="card card--back" aria-label="Business card back">
    <svg class="corner-flag corner-flag--top" width="40" height="52" viewBox="0 0 40 52"><polygon points="0,0 40,26 0,52" fill="var(--brand-red)"/></svg>
    <svg class="corner-flag corner-flag--bottom" width="40" height="52" viewBox="0 0 40 52"><polygon points="40,0 0,26 40,52" fill="var(--brand-red)"/></svg>

    <div class="brand-name"><span class="brand-dot"></span>BrindleStaffing</div>

    <h1 class="person-name">Gregory Malden</h1>
    <p class="person-title">Chairman</p>

    <ul class="contact-list">
      <li class="contact-item">
        <svg class="contact-icon" viewBox="0 0 30 30"><polygon points="15,1 28,8 28,22 15,29 2,22 2,8" fill="var(--brand-red)"/><path d="M10 9c1-1 2-1 2.5 0l1.3 2.5c.3.7 0 1.3-.6 1.7l-.7.5c.8 1.8 2 3 3.8 3.8l.5-.7c.4-.6 1-.9 1.7-.6l2.5 1.3c1 .5 1 1.5 0 2.5-1.2 1.2-3 1.4-5 .3-3-1.6-5.2-3.8-6.8-6.8-1.1-2-.9-3.8.3-5z" fill="#fff"/></svg>
        813-555-0147 <span class="contact-label">Mobile</span>
      </li>
      <li class="contact-item">
        <svg class="contact-icon" viewBox="0 0 30 30"><polygon points="15,1 28,8 28,22 15,29 2,22 2,8" fill="var(--brand-red)"/><rect x="10.5" y="8" width="9" height="5" fill="none" stroke="#fff" stroke-width="1.5"/><rect x="8" y="13" width="14" height="6" rx="1" fill="#fff"/><rect x="10.5" y="17" width="9" height="5" fill="var(--brand-red)" stroke="#fff" stroke-width="1.5"/></svg>
        813-555-0183 <span class="contact-label">Fax</span>
      </li>
      <li class="contact-item">
        <svg class="contact-icon" viewBox="0 0 30 30"><polygon points="15,1 28,8 28,22 15,29 2,22 2,8" fill="var(--brand-red)"/><rect x="8" y="10" width="14" height="10" rx="1" fill="none" stroke="#fff" stroke-width="1.6"/><path d="M8 10.5l7 5.5 7-5.5" fill="none" stroke="#fff" stroke-width="1.6"/></svg>
        gmalden@brindlestaffing.example
      </li>
      <li class="contact-item">
        <svg class="contact-icon" viewBox="0 0 30 30"><polygon points="15,1 28,8 28,22 15,29 2,22 2,8" fill="var(--brand-red)"/><circle cx="15" cy="15" r="7" fill="none" stroke="#fff" stroke-width="1.6"/><path d="M8 15h14M15 8c-3 4-3 10 0 14M15 8c3 4 3 10 0 14" fill="none" stroke="#fff" stroke-width="1.3"/></svg>
        www.brindlestaffing.example
      </li>
    </ul>

    <div class="address-band">
      <svg viewBox="0 0 12 16"><path d="M6 0a6 6 0 0 0-6 6c0 4.5 6 10 6 10s6-5.5 6-10a6 6 0 0 0-6-6zm0 8.5a2.5 2.5 0 1 1 0-5 2.5 2.5 0 0 1 0 5z" fill="#fff"/></svg>
      417 39th Crescent South, Saint Petersburg FL 33719
    </div>
  </section>

</main>
</body>
</html>
```